Yoga Instrucor

I need my personal business cards, i would like the front a kind of light but vibrant red and matt gold.

Industry/Entity Type

Business

Contact Information for Business Card

Cordelia Hastrup
Yoga Instructor
RYT 200, BROKU (NYC) Yoga RYT 500,
CPR/ AED Certified,
hastrupcordelia@quillbox.com
512 604 8893
Adult Yoga, Private Yoga, Group Classes, Restorative, Meditation, Child Yoga.

```html
<!DOCTYPE html>
<html lang="en">
<head>
<meta charset="utf-8">
<title>Cordelia Hastrup — Yoga Instructor</title>
<link rel="stylesheet" href="https://fonts.googleapis.com/css2?family=Gochi+Hand&display=swap">
<style>
  :root {
    --card-red: #ff0012;
    --figure-shade: #e8000f;
    --matt-gold: #ff9c00;
    --canvas-w: 1200px;
    --canvas-h: 702px;
  }
  html, body {
    margin: 0;
    padding: 0;
    width: var(--canvas-w);
    height: var(--canvas-h);
    overflow: hidden;
    background: var(--card-red);
  }
  .business-card {
    position: relative;
    width: var(--canvas-w);
    height: var(--canvas-h);
    background: var(--card-red);
    font-family: "Gochi Hand", cursive;
    color: var(--matt-gold);
    overflow: hidden;
  }
  .pose-illustration-large {
    position: absolute;
    left: 885px;
    top: 0;
    width: 265px;
    height: 702px;
    border-radius: 120px 120px 60px 60px;
    background: linear-gradient(180deg, rgba(200,0,10,0) 0%, var(--figure-shade) 20%, var(--figure-shade) 80%, rgba(200,0,10,0) 100%);
  }
  .holder-name {
    position: absolute;
    left: 0;
    right: 0;
    top: 175px;
    margin: 0;
    text-align: center;
    font-weight: 400;
    font-size: 132px;
    line-height: 1;
    letter-spacing: 2px;
    white-space: nowrap;
  }
  .pose-illustration-small {
    display: inline-block;
    width: 62px;
    height: 240px;
    margin: 0 8px;
    vertical-align: -50px;
    border-radius: 30px;
    background: linear-gradient(180deg, rgba(255,156,0,0.55), rgba(255,156,0,0.35));
  }
  .holder-role {
    position: absolute;
    left: 404px;
    top: 395px;
    margin: 0;
    font-size: 68px;
    font-weight: 400;
    line-height: 1;
    letter-spacing: 2px;
  }
  .contact-email,
  .contact-phone {
    position: absolute;
    top: 580px;
    font-size: 48px;
    line-height: 1;
    letter-spacing: 2px;
  }
  .contact-email { left: 74px; }
  .contact-phone { right: 72px; font-size: 46px; }
</style>
</head>
<body>
  <main class="business-card">
    <div class="pose-illustration-large" role="img" aria-label="Large faint line drawing of a woman in tree pose with arms raised"></div>

    <h1 class="holder-name">Corde<span class="pose-illustration-small" role="img" aria-label="Small line drawing of a woman in tree pose standing in for the letter l"></span>ia Hastrup</h1>

    <p class="holder-role">yoga instructor</p>

    <span class="contact-email">hastrupcordelia@quillbox.com</span>
    <span class="contact-phone">512-604-8893</span>
  </main>
</body>
</html>
```